Church needs a street sign design

We're a small church located in Silicon Valley, California. Our website is https://www.hpkwendell.org/ and our address is 1847 Thornby Ave, San Jose, California, 95871. You can look up our location on Google Maps to see the sign from Street View. I have uploaded an image of the street sign as well. The marquee, the top section of the sign, and the separating line between them both will be removed. We're seeking a design for a new backlit acrylic insert that will go on the front of the light box and the back of the lightbox. The acrylic sign will fill the entire external frame. In the future, we may build a decorative wood frame around the structural legs, as visualized in one of the uploaded files. The church's brand colors are: #003366 (dark blue), #ff6600 (vibrant orange), #228b22 (forest green). I have also uploaded the church's logo assets. Our primary font is Montserrat and the secondary is Poppins. You can deviate from these colors/fonts if the sign is still coherent with the rest of our branding. Our branding values are mission, truth, passion, and community (please do not put those words on the sign! They are just intended to guide the look of the design). The sign dimensions are 96" by 47.5". Keep in mind that the sign will be backlit on a busy street side. It will also be positioned next to an old-looking church building. We do NOT want a sign that looks traditional, old, or antiquated. Instead, we want a modern-looking sign that pairs well with our old building while helping it look more modern too. We would also like the web address clearly visible on the sign: hpkwendell.org. If you have any questions, just let me know!

```html
<!DOCTYPE html>
<html lang="en">
<head>
<meta charset="utf-8">
<title>Wendell Fellowship Church – Street Sign</title>
<link rel="stylesheet" href="https://fonts.googleapis.com/css2?family=Montserrat:wght@500;600&family=Poppins:wght@600;700;800&family=Yellowtail&display=swap">
<style>
  :root {
    --page-bg: #b9b9b9;
    --brand-navy: #0a2850;
    --brand-blue: #003366;
    --brand-orange: #ff6600;
    --ink: #222222;
    --paper: #ffffff;
    --photo-top: #4d6d93;
    --photo-mid: #3a5a80;
    --photo-bottom: #1f3a5f;
  }
  * { margin: 0; padding: 0; box-sizing: border-box; }
  html, body {
    width: 1200px; height: 922px; overflow: hidden;
    background: var(--page-bg);
  }
  .sign {
    position: absolute; left: 30px; top: 179px;
    width: 1140px; height: 564px; overflow: hidden;
  }
  .city-photo {
    position: absolute; inset: 0;
    background: linear-gradient(180deg, var(--photo-top) 0%, var(--photo-mid) 45%, var(--photo-bottom) 100%);
  }
  .panels { position: absolute; inset: 0; }
  .church-name {
    position: absolute; left: 46px; top: 92px;
    display: flex; align-items: center; gap: 24px;
    color: var(--paper);
    font-family: "Montserrat", sans-serif; font-weight: 500;
  }
  .church-name__mark {
    width: 44px; height: 44px; background: var(--paper);
  }
  .church-name__text { line-height: 1; }
  .church-name__primary { display: block; font-size: 56px; letter-spacing: 1px; }
  .church-name__secondary { display: block; font-size: 21px; letter-spacing: 1px; margin-top: 12px; }
  .headline {
    position: absolute; left: 684px; width: 414px; text-align: center;
    font-family: "Poppins", sans-serif; line-height: 1;
  }
  .headline--main {
    top: 82px; font-size: 102px; font-weight: 800;
    color: var(--brand-blue); letter-spacing: -5px;
  }
  .headline--sub {
    top: 175px; font-size: 50px; font-weight: 700;
    color: var(--ink); letter-spacing: -1.5px;
  }
  .tagline {
    position: absolute; left: 544px; top: 262px; width: 567px; text-align: center;
    font-family: "Yellowtail", cursive; font-size: 78px; line-height: 90px;
    color: var(--paper);
  }
  .web-address {
    position: absolute; left: 500px; top: 462px; width: 608px; text-align: right;
    font-family: "Poppins", sans-serif; font-weight: 600; font-size: 48px;
    letter-spacing: 3px; color: var(--paper); line-height: 1;
  }
  .web-address__domain { color: var(--brand-orange); }
</style>
</head>
<body>
  <main class="sign">
    <div class="city-photo" role="img" aria-label="Blue-toned aerial photo of the San Jose skyline with mountains behind and tree-lined neighbourhoods in front"></div>

    <svg class="panels" width="1140" height="564" viewBox="0 0 1140 564" aria-hidden="true">
      <polygon class="panel-white" fill="var(--paper)"
        points="727,0 1140,0 1140,410 518,410 530,384 540,380 548,350 560,340 572,310 590,300 600,270 612,262 640,255 650,240 662,226 672,200 682,170 694,150 705,118 712,92 720,60 722,30"/>
      <polygon class="panel-navy" fill="var(--brand-navy)"
        points="518,412 540,404 580,406 620,400 660,403 700,398 760,401 800,397 860,402 920,396 980,401 1020,396 1060,400 1100,397 1140,404 1140,564 391,564 410,530 430,500 448,470 470,450 490,430"/>
      <polygon class="brush-stroke" fill="var(--brand-orange)"
        points="560,268 600,262 700,264 760,259 840,262 920,258 1000,262 1060,258 1104,262 1100,276 1111,290 1098,302 1108,318 1096,330 1106,344 1090,356 1000,353 920,358 840,354 760,358 680,353 600,357 566,352 574,340 556,330 570,318 548,306 566,296 544,282"/>
    </svg>

    <div class="church-name">
      <span class="church-name__mark"></span>
      <span class="church-name__text">
        <span class="church-name__primary">WENDELL</span>
        <span class="church-name__secondary">FELLOWSHIP CHURCH</span>
      </span>
    </div>

    <h1 class="headline headline--main">JOIN US</h1>
    <p class="headline headline--sub">AS WE FOLLOW</p>
    <p class="tagline">Jesus together</p>
    <p class="web-address">www.<span class="web-address__domain">hpkwendell</span>.org</p>
  </main>
</body>
</html>
```